Corporate Identity Design Project

Marisol Tevendry Design is a small boutique event planning and floral design company, based in Northern Alberta. I require the creation of some corporate identity pieces. I want a minimalistic design.
Website www.marisoltevendry.com

Pieces should include
1. Business Card
Should include the company logo, name, email address, address, phone number. These will be professional printed.
These are three cards that I like:
http://cardlayoutgallerynook.com/wp-content/uploads/2010/02/Renata_Voskuilen_Roomworks_by_Pepperleaf_studio_Graphics.jpg
http://tidycardshowcase.com/wp-content/uploads/2011/06/Quietfold-Studio-Minimalist-Business-Cards_11.jpg
http://graphiclanternhub.com/wp-content/uploads/2012/03/16.minimalist-business-cards.jpg
I like letterpress, but I am open to other options.

2. Letterhead
will be professionally printed

3. Envelope

4. Fax Sheet
will be printed on home printer

5. Pocket Presentation
Like -http://fernwickgardenworks.com/img/design_step_proposal@2x.jpg

6. Invoice
Like - http://velmaquorlin.files.blogsite-example.com/2011/02/summit-strength-4-letterhead-combined.png?w=529

7. Proposal
Like something like this – this will not be printed, but rather emailed to clients
Like http://getfile7.brindlepost.com/getfile/files.brindlepost.com/tarnu-studio/qwRtZe8MmXp3LoKcV7B2nhdYJsaWeFUy6gT4rkPHvxiQbNcDzA9jsLE/Picture-52.png.scaled.500.jpg

8. Contract
Like http://www.brightkeelpromo.co.uk/images/tamsin-contract.jpg

9. Business Brochure – I have removed this piece from the project and will most likely post it as another project at a later date.

If you think that this is a project of interest to you, but feel that it is “too much” work for the price, please let me know how you would re-package it – I am open to suggestions.

Target Market(s)

Young women

Industry/Entity Type

Boutique

Requirements
Should not have
• I do not want it to look "frilly"

```html
<!DOCTYPE html>
<html lang="en">
<head>
<meta charset="utf-8">
<title>Marisol Tevendry Design — Stationery Set</title>
<link href="https://fonts.googleapis.com/css2?family=Josefin+Sans:wght@600&family=Questrial&display=swap" rel="stylesheet">
<style>
:root{
  --bg-top:#f6f6fc;
  --bg-bottom:#e9e8f6;
  --ink:#0b0b0d;
  --pink:#e5099b;
  --paper:#ffffff;
  --paper-soft:#fbfbfe;
  --grey:#6a6a72;
  --logo-light:#d9d9de;
  --label:#2a2a2e;
  --photo-a:#26198a;
  --photo-b:#5a49c6;
  --photo-c:#e8e6f2;
}
*{margin:0;padding:0;box-sizing:border-box}
html,body{width:1200px;height:1200px;overflow:hidden}
body{
  position:relative;
  background:linear-gradient(180deg,var(--bg-top),var(--bg-bottom));
  font-family:"Questrial",sans-serif;
  color:var(--ink);
}
.piece{position:absolute;box-shadow:0 6px 14px rgba(20,20,40,.28)}
.flap{position:absolute;background:var(--pink)}

.brand{position:absolute;display:flex;align-items:center;gap:6px}
.brand-dot{border-radius:50%;background:currentColor;flex:none}
.brand-name{
  font-family:"Josefin Sans",sans-serif;font-weight:600;
  text-transform:uppercase;letter-spacing:.14em;line-height:1.05;
}
.brand.dark{color:var(--ink)}
.brand.light{color:var(--logo-light)}

.contact{position:absolute;font-size:4.2px;line-height:6px;color:var(--grey)}
.contact li{list-style:none;display:flex;align-items:center;gap:3px;white-space:nowrap}
.contact li::before{content:"";width:3px;height:3px;background:currentColor;border-radius:1px}

.copy{position:absolute;font-size:4px;line-height:5.3px;color:#555;text-align:justify}
.copy p+p{margin-top:5px}

/* side labels */
.label{
  position:absolute;font-size:19px;font-style:italic;color:var(--label);
  writing-mode:vertical-rl;transform:rotate(180deg);white-space:nowrap;line-height:22px;
}
.label-line{position:absolute;width:1px;background:var(--label)}

.envelope{left:114px;top:258px;width:312px;height:209px;background:var(--paper)}
.envelope .flap{left:0;top:0;width:100%;height:52px;clip-path:polygon(7% 0,93% 0,100% 100%,0 100%)}

.folder{left:437px;top:128px;width:298px;height:469px;box-shadow:none}
.folder .flap{left:0;top:0;width:100%;height:53px;clip-path:polygon(10% 0,90% 0,100% 100%,0 100%)}
.folder-body{position:absolute;left:0;top:52px;width:100%;height:417px;background:var(--ink);box-shadow:0 6px 14px rgba(20,20,40,.35)}

.card-front{left:129px;top:499px;width:255px;height:141px;background:var(--ink)}
.card-back{left:129px;top:665px;width:255px;height:141px;background:var(--ink)}
.card-back-inner{position:absolute;left:5px;top:5px;right:5px;bottom:5px;background:var(--paper)}
.corner{position:absolute;background:var(--pink)}

.letterhead{left:761px;top:178px;width:297px;height:419px;background:var(--paper)}
.sign{position:absolute;font-size:4px;color:#777;line-height:5px}
.rule{position:absolute;height:4px;background:var(--pink)}

.proposal{left:437px;top:627px;width:298px;height:421px;background:var(--paper);overflow:hidden}
.photo{position:absolute;left:0;top:0;width:100%;height:138px;
  background:linear-gradient(90deg,var(--photo-a) 0%,var(--photo-b) 35%,var(--photo-c) 50%,var(--photo-b) 65%,var(--photo-a) 100%)}
.photo-tag{position:absolute;left:0;top:73px;width:128px;height:60px;background:rgba(90,80,170,.55)}
.side-col{position:absolute;left:0;top:145px;width:133px;height:276px;background:var(--ink)}
.side-word{position:absolute;left:86px;top:400px;transform:rotate(-90deg);transform-origin:left top;
  font-size:38px;font-weight:700;color:var(--paper);letter-spacing:.01em;white-space:nowrap}
.section-title{position:absolute;left:152px;top:156px;font-size:19px;color:var(--ink)}

.invoice{left:761px;top:627px;width:297px;height:421px;background:var(--paper-soft);overflow:hidden}
.invoice-head{position:absolute;left:0;top:0}

.corner-tag{position:absolute;left:0;top:1078px;width:272px;height:122px;background:var(--ink);
  clip-path:polygon(0 0,150px 0,272px 122px,0 122px)}
</style>
</head>
<body>

<!-- labels -->
<div class="label-line" style="left:82px;top:258px;height:112px"></div>
<div class="label" style="left:70px;top:380px">envelope</div>
<div class="label-line" style="left:100px;top:499px;height:178px"></div>
<div class="label" style="left:89px;top:688px">business card</div>
<div class="label-line" style="left:1085px;top:178px;height:312px"></div>
<div class="label" style="left:1074px;top:500px">letterhead</div>
<div class="label-line" style="left:408px;top:627px;height:333px"></div>
<div class="label" style="left:397px;top:970px">proposal</div>
<div class="label-line" style="left:1085px;top:627px;height:348px"></div>
<div class="label" style="left:1074px;top:985px">invoice</div>

<!-- envelope -->
<section class="piece envelope">
  <div class="flap"></div>
  <div class="brand dark" style="left:12px;top:72px">
    <span class="brand-dot" style="width:14px;height:14px"></span>
    <span class="brand-name" style="font-size:6.5px">Marisol<br>Tevendry<br>Design</span>
  </div>
  <ul class="contact" style="left:9px;top:180px">
    <li>marisol tevendry</li>
    <li>info@marisoltevendry.com</li>
    <li>0147258360</li>
    <li>27 harrowgate lane 4716</li>
  </ul>
</section>

<!-- business cards -->
<section class="piece card-front">
  <div class="brand light" style="left:62px;top:48px">
    <span class="brand-dot" style="width:30px;height:30px;opacity:.8"></span>
    <span class="brand-name" style="font-size:10px">Marisol<br>Tevendry<br>Design</span>
  </div>
</section>
<section class="piece card-back">
  <div class="corner" style="left:0;top:95px;width:5px;height:46px"></div>
  <div class="corner" style="left:0;bottom:0;width:50px;height:5px;clip-path:polygon(0 0,90% 0,100% 100%,0 100%)"></div>
  <div class="corner" style="right:0;top:0;width:45px;height:5px;clip-path:polygon(0 0,100% 0,100% 100%,10% 100%)"></div>
  <div class="corner" style="right:0;top:0;width:5px;height:45px"></div>
  <div class="card-back-inner">
    <div class="brand dark" style="left:38px;top:40px">
      <span class="brand-dot" style="width:16px;height:16px"></span>
      <span class="brand-name" style="font-size:7px">Marisol<br>Tevendry<br>Design</span>
    </div>
    <ul class="contact" style="left:124px;top:58px;font-size:5px;line-height:7.5px">
      <li>marisol tevendry</li>
      <li>info@marisoltevendry.com</li>
      <li>0147258360</li>
      <li>27 harrowgate lane 4716</li>
    </ul>
  </div>
</section>

<!-- pocket folder -->
<section class="piece folder">
  <div class="flap"></div>
  <div class="folder-body">
    <div class="brand light" style="left:92px;top:165px">
      <span class="brand-dot" style="width:36px;height:36px;opacity:.8"></span>
      <span class="brand-name" style="font-size:10px">Marisol<br>Tevendry<br>Design</span>
    </div>
  </div>
</section>

<!-- letterhead -->
<section class="piece letterhead">
  <div class="brand dark" style="left:26px;top:28px">
    <span class="brand-dot" style="width:14px;height:14px"></span>
    <span class="brand-name" style="font-size:6px">Marisol<br>Tevendry<br>Design</span>
  </div>
  <ul class="contact" style="left:169px;top:47px;font-size:3.6px;line-height:5px">
    <li>marisol tevendry</li><li>0147258360</li>
  </ul>
  <ul class="contact" style="left:218px;top:47px;font-size:3.6px;line-height:5px">
    <li>info@marisoltevendry.com</li><li>27 harrowgate lane 4716</li>
  </ul>
  <div class="copy" style="left:24px;top:90px;width:245px">
    <p>Thank you for choosing us to plan your celebration. We are delighted to share the details of our floral and event services with you. Every piece is shaped around your vision, your season and your venue, with calm planning from the first meeting to the last petal. We begin by learning about the people at the heart of the day, the places that matter to them and the feeling they want their guests to carry home. From there we build a plan that is simple to follow and easy to adjust as ideas grow and change over the coming months.</p>
    <p>Our team will prepare a full timeline, a colour study and a list of seasonal blooms for your review. We will meet again to confirm each choice before any order is placed, so nothing arrives that you have not seen and approved. You will also receive a short guide to the suppliers we trust, along with notes on timing, delivery and set up for each part of the event, from the ceremony space to the final table of the evening.</p>
    <p>Please find the proposed schedule and fees enclosed. Deposits secure your date, and the balance is due two weeks before the event. Should your plans change, we are happy to revise the estimate and the timeline at any point before final orders are placed with our growers and rental partners. Every revision is shared in writing so both sides always hold the same clear picture of the work ahead.</p>
    <p>On the day itself our crew arrives early to place every arrangement, check the lighting and walk the room with your coordinator. We remain on site through the ceremony and return at the close of the evening to clear each space, leaving the venue exactly as we found it. Any flowers you wish to keep are wrapped and ready to travel home with you or your family.</p>
    <p>We look forward to working with you and to making the day feel simple, bright and entirely yours. If you have any questions about this letter or the enclosed estimate, please reach out by phone or email at any time and we will reply within one working day.</p>
  </div>
  <div class="sign" style="left:24px;top:317px">Yours Sincerely,</div>
  <span style="position:absolute;left:30px;top:333px;width:10px;height:10px;border-radius:50%;background:var(--pink)"></span>
  <div class="sign" style="left:24px;top:355px">Marisol Tevendry<br>Design</div>
  <div class="rule" style="left:24px;top:402px;width:246px"></div>
</section>

<!-- proposal -->
<section class="piece proposal">
  <div class="photo" role="img" aria-label="Bridesmaids in violet dresses holding blue orchid bouquets beside a bride in white"></div>
  <div class="photo-tag">
    <div class="brand light" style="left:10px;top:14px;color:#fff">
      <span class="brand-dot" style="width:22px;height:22px;opacity:.85"></span>
      <span class="brand-name" style="font-size:7.5px">Marisol<br>Tevendry<br>Design</span>
    </div>
  </div>
  <div class="side-col"></div>
  <span style="position:absolute;left:98px;top:238px;width:10px;height:10px;border-radius:50%;background:var(--paper)"></span>
  <div class="side-word">working</div>
  <div class="rule" style="left:133px;top:145px;width:145px;height:6px"></div>
  <div class="section-title">work method</div>
  <div class="copy" style="left:152px;top:192px;width:130px">
    <p>Every event begins with a quiet conversation. We listen to your plans, your guest list and the mood you hope to create, then sketch a first outline of colours, flowers and space. This early stage is relaxed and open, and there is no wrong idea. We gather images, fabrics and small samples so that you can see and touch the direction before any decision is fixed. By the end you hold a short brief that guides every later step.</p>
    <p>Next we visit the venue, measure tables, aisles and doorways, and build a floral plan that suits the light and the season. We note where guests will gather, where photos will be taken and how the room will feel as the evening changes. You then receive a clear written estimate with every item listed, so the budget is easy to read and simple to adjust if needed.</p>
    <p>Once approved, we order blooms, book rentals and confirm every supplier, keeping you informed each week. A shared timeline shows what is done and what comes next, and we answer questions quickly so that nothing waits on a reply.</p>
    <p>On the day we arrive early, set each piece with care and stay close until the last guest has gone home, then clear every space.</p>
  </div>
</section>

<!-- invoice -->
<section class="piece invoice">
  <svg class="invoice-head" width="297" height="100" viewBox="0 0 297 100" aria-hidden="true">
    <path d="M0 0H297V62Q150 60 0 88Z" fill="var(--ink)"/>
    <path d="M0 84Q150 56 297 60V64Q150 62 0 90Z" fill="var(--pink)"/>
  </svg>
  <div class="brand light" style="left:14px;top:14px;color:#fff">
    <span class="brand-dot" style="width:15px;height:15px"></span>
    <span class="brand-name" style="font-size:6.5px">Marisol<br>Tevendry<br>Design</span>
  </div>
  <ul class="contact" style="left:182px;top:31px;font-size:3.6px;line-height:5px;color:#bbb">
    <li>marisol tevendry</li><li>0147258360</li>
  </ul>
  <ul class="contact" style="left:228px;top:31px;font-size:3.6px;line-height:5px;color:#bbb">
    <li>info@marisoltevendry.com</li><li>27 harrowgate lane 4716</li>
  </ul>
  <span style="position:absolute;left:257px;top:370px;width:14px;height:14px;border-radius:50%;background:var(--pink)"></span>
</section>

<!-- presenter corner -->
<div class="corner-tag">
  <div class="brand light" style="left:24px;top:28px">
    <span class="brand-dot" style="width:40px;height:40px;opacity:.8"></span>
    <span class="brand-name" style="font-size:12px">Marisol<br>Tevendry<br>Design</span>
  </div>
</div>

</body>
</html>
```